Award-winnning Estate Agent needs a premium version of their 'For Sale' board design

We need a premium option for our 'For Sale' board design. We have a standard board that is attached to this brief, but were are looking to have a premium design version that we will use when selling exclusive properties. Our company name is Harbourline Row Estates and the name for this is exclusive selection is: 'The Harbourline Portfolio'. The design needs to work with our current brand, but have a distinctive PREMIUM feel to it. I have uploaded the barnd guidelines and also some of the exisisting logo variations. We do NOT need a new logo but feel free to play around with colours, fonts, sizes etc. for the sign.

Target Market(s)

Property buyers & house hunters

Industry/Entity Type

Real Estate - Residential Property

Font styles to use
Sans Serif

Requirements
Must have
• A premium fee, must be square design, must be easy to read when driving past the sign
Nice to have
• I'm open ot ideas

```html
<!DOCTYPE html>
<html lang="en">
<head>
<meta charset="utf-8">
<title>Harbourline Row Estates – The Harbourline Portfolio For Sale Board</title>
<link rel="stylesheet" href="https://fonts.googleapis.com/css2?family=Inter:wght@300;600;800&display=swap">
<style>
  :root {
    --brand-navy: #2b3a8f;
    --brand-blue: #1a75bc;
    --silver-light: #f7f7f8;
    --silver-mid: #e3e4e6;
    --silver-deep: #cbccd0;
    --ink: #050505;
    --title-grey: #5b5b5e;
    --divider-grey: #6e6e70;
  }
  html, body {
    margin: 0;
    padding: 0;
    width: 1200px;
    height: 1200px;
    overflow: hidden;
    background: #ffffff;
  }
  .sale-board {
    display: block;
    width: 1200px;
    height: 1200px;
  }
  .brand-name {
    font-family: "Inter", sans-serif;
    font-weight: 600;
    fill: var(--brand-navy);
  }
  .portfolio-title {
    font-family: "Inter", sans-serif;
    font-weight: 300;
    fill: var(--title-grey);
  }
  .sale-headline {
    font-family: "Inter", sans-serif;
    font-weight: 800;
    fill: var(--ink);
  }
  .sale-phone {
    font-family: "Inter", sans-serif;
    font-weight: 300;
    fill: var(--ink);
  }
  .sale-website {
    font-family: "Inter", sans-serif;
    font-weight: 300;
    fill: var(--title-grey);
  }
</style>
</head>
<body>
<svg class="sale-board" viewBox="0 0 1200 1200" xmlns="http://www.w3.org/2000/svg">
  <defs>
    <linearGradient id="silver-base" x1="0" y1="0" x2="0" y2="1">
      <stop offset="0" stop-color="var(--silver-deep)"/>
      <stop offset="0.55" stop-color="#d6d7da"/>
      <stop offset="1" stop-color="var(--silver-mid)"/>
    </linearGradient>
    <radialGradient id="silver-glow-top" cx="0.3" cy="0.15" r="0.45">
      <stop offset="0" stop-color="#ffffff" stop-opacity="1"/>
      <stop offset="0.5" stop-color="#f0f0f1" stop-opacity="0.7"/>
      <stop offset="1" stop-color="#ffffff" stop-opacity="0"/>
    </radialGradient>
    <radialGradient id="silver-glow-bottom" cx="0.6" cy="0.95" r="0.4">
      <stop offset="0" stop-color="#ffffff" stop-opacity="0.85"/>
      <stop offset="1" stop-color="#ffffff" stop-opacity="0"/>
    </radialGradient>
  </defs>

  <g class="board-background" role="img" aria-label="Brushed silver background with a faint skyline of a tower and rooftops">
    <rect width="1200" height="1200" fill="url(#silver-base)"/>
    <rect width="1200" height="1200" fill="url(#silver-glow-top)"/>
    <rect width="1200" height="1200" fill="url(#silver-glow-bottom)"/>
  </g>

  <g class="brand-block">
    <rect class="brand-square" x="215" y="96" width="84" height="84" fill="var(--brand-blue)"/>
    <text class="brand-name" x="62" y="256" font-size="36" textLength="400" lengthAdjust="spacingAndGlyphs">Harbourline Row Estates</text>
  </g>

  <line class="header-divider" x1="511" y1="29" x2="511" y2="297" stroke="var(--divider-grey)" stroke-width="2"/>

  <g class="portfolio-title" font-size="90">
    <text x="556" y="140" textLength="580" lengthAdjust="spacingAndGlyphs">The Harbourline</text>
    <text x="556" y="258">Portfolio</text>
  </g>

  <text class="sale-headline" x="62" y="775" font-size="214" textLength="1076" lengthAdjust="spacingAndGlyphs">FOR SALE</text>

  <rect class="headline-rule" x="62" y="816" width="1076" height="5" fill="var(--ink)"/>

  <text class="sale-phone" x="62" y="969" font-size="158" textLength="1071" lengthAdjust="spacingAndGlyphs">01632  960418</text>

  <text class="sale-website" x="600" y="1167" font-size="44" text-anchor="middle" textLength="670" lengthAdjust="spacingAndGlyphs">www.harbourlinerowestates.co.uk</text>
</svg>
</body>
</html>
```